International industry company needs New Email Marketing Design

We need a new Email Marketing Design with the content in the attachment (html file).

Target Market(s)

engineers, technical directors, technologists, scientists from the aviation, defense, space and energy industries.

Font styles to use
Sans Serif

Requirements
Must have
• brio.vantel logo
photo of a gas turbine.
Should not have
• it cannot contain elements indicating material testing

```html
<!DOCTYPE html>
<html lang="en">
<head>
<meta charset="utf-8">
<title>brio.vantel – Machining of Specimens &amp; Test Samples</title>
<link href="https://fonts.googleapis.com/css2?family=Hind:wght@400;500;600&display=swap" rel="stylesheet">
<style>
:root{
  --blue:#3a58a0;
  --orange:#f39200;
  --yellow:#fdc800;
  --ink:#2a2a2a;
  --muted:#555;
  --dark:#2b2d35;
  --white:#fff;
}
*{margin:0;padding:0;box-sizing:border-box}
html,body{width:1200px;height:3705px;overflow:hidden;background:#fff}
body{position:relative;font-family:"Hind",sans-serif;color:var(--ink)}
.abs{position:absolute}
.hero{left:0;top:0;width:1200px;height:825px;
  background:radial-gradient(ellipse 220px 420px at 590px 380px,#e9783a 0%,#a5482a 35%,transparent 70%),
  linear-gradient(100deg,#4a4d55 0%,#6f737b 35%,#3b3d44 60%,#55575e 100%)}
.logo{font-weight:500;font-size:39px;line-height:1;color:var(--blue);letter-spacing:.5px;display:flex;align-items:center;gap:10px}
.logo .dot{width:14px;height:14px;background:var(--orange)}
.logo-hero{left:158px;top:26px;color:#7f9bd8}
.logo-footer{left:148px;top:3265px;font-size:46px}
.hero-social{right:165px;top:30px;display:flex;gap:14px}
.hero-social span{width:28px;height:28px;border-radius:3px}
.hero-title{left:0;width:1200px;top:362px;text-align:center;color:var(--white);font-weight:500;font-size:60px;line-height:75px}
.intro{left:148px;top:673px;width:903px;height:367px;background:var(--blue);color:var(--white);text-align:center;padding:38px 70px 0}
.intro h1{font-weight:500;font-size:34px;margin-bottom:30px}
.intro p{font-size:23.5px;line-height:37.5px}
.lead{left:0;width:1200px;top:1108px;text-align:center;font-size:24px;font-weight:500}
.uses{left:148px;top:1196px;list-style:none;font-size:21px;line-height:46.5px}
.uses li,.acc-text li{padding-left:30px;position:relative}
.uses li::before,.acc-text li.mark::before{content:"";position:absolute;left:2px;top:18px;width:9px;height:9px;background:var(--orange)}
.samples{left:645px;top:1255px;width:365px;height:430px;border-radius:6px;background:linear-gradient(160deg,#f2f2f3,#c9cacd 55%,#eeeeef)}
.btn-wide{left:148px;top:1785px;width:903px;height:60px;border-radius:4px;background:var(--blue);color:var(--white);font-size:20.5px;font-weight:600;display:flex;align-items:center;justify-content:center}
.values{left:0;top:1935px;width:1200px;height:225px;background:var(--orange);display:flex;justify-content:space-between;align-items:center;padding:0 150px}
.value{display:flex;align-items:center;gap:16px;color:var(--white);font-size:25px;font-weight:500}
.acc-title{left:0;width:1200px;top:2250px;text-align:center;font-size:24.5px;font-weight:500}
.acc-img{left:150px;top:2345px;width:380px;height:335px;border-radius:50%;background:radial-gradient(circle at 55% 50%,#b7bcc6 0%,#7d8aa8 40%,#3a58a0 62%)}
.acc-text{left:600px;top:2368px;font-size:21px;line-height:46.5px}
.acc-text ul{list-style:none}
.contact{left:0;top:2835px;width:1200px;height:345px;background:var(--yellow)}
.contact p{left:148px;top:80px;color:var(--white);font-size:28px;font-weight:500;line-height:45px;letter-spacing:1.5px}
.btn-contact{left:148px;top:198px;width:210px;height:60px;background:var(--blue);border-radius:3px;color:var(--white);font-size:21px;font-weight:500;display:flex;align-items:center;justify-content:center}
.agent{left:705px;top:2760px;width:285px;height:420px;border-radius:140px 140px 0 0;background:linear-gradient(180deg,#e8d4c4 0%,#3a3a3f 45%,#2a2a30 100%)}
.co{left:150px;top:3330px;font-size:17px;line-height:38px;color:var(--muted)}
.foot-social{left:152px;top:3437px;display:flex;gap:100px}
.foot-social span{width:30px;height:30px;border-radius:4px}
.info{left:653px;top:3330px;font-size:17px;line-height:40.5px;color:var(--muted);list-style:none}
.info li{display:flex;align-items:center;gap:16px}
.info li.cont{padding-left:42px}
.bottom{left:0;top:3558px;width:1200px;height:147px;background:var(--dark);display:flex;justify-content:space-between;align-items:center;padding:0 150px;font-size:17px}
.bottom .copy{color:var(--white);font-weight:500}
.bottom .unsub{color:var(--orange)}
</style>
</head>
<body>
<section class="abs hero" role="img" aria-label="Photo of a glowing gas turbine component during machining"></section>
<div class="abs logo logo-hero"><span class="dot"></span>brio.vantel</div>
<div class="abs hero-social"><span style="background:#b42a1e"></span><span style="background:#2166a8"></span></div>
<h2 class="abs hero-title">MACHINING OF SPECIMENT &amp;<br>TEST SAMPLES</h2>

<section class="abs intro">
  <h1>Dear Surface Coatings Society Members,</h1>
  <p>Ferrovane manufactures high quality test coupons, specimens, samples, buttons, panels, discs, and strips for Thermal and Cold Spray facilities mainly in the aviation industry. We specialize in cutting difficult-to-machine aerospace grade materials such as nickel &amp; cobalt base superalloys, titanium, and hardened steel.</p>
</section>

<p class="abs lead">Our experience includes manufacturing specimens used for:</p>
<ul class="abs uses">
  <li>Adhesion, cohesive and bond strength<br>test of coating</li>
  <li>Tensile test</li>
  <li>Hardness test</li>
  <li>Microstructure evaluation</li>
  <li>Fatigue test</li>
  <li>Lap shear test</li>
  <li>Bend test</li>
  <li>Erosion test</li>
  <li>Stress corrosion test</li>
  <li>Hoffman Scratch test</li>
  <li>The cyclic furnace oxidation test (FCT)</li>
</ul>
<div class="abs samples" role="img" aria-label="Photo of machined metal specimens: threaded bar, plates, disc and flat strip"></div>
<div class="abs btn-wide">Read more about our test coupons and spesimens here!</div>

<section class="abs values">
  <div class="value">
    <svg width="62" height="90" viewBox="0 0 62 90"><circle cx="31" cy="31" r="26" fill="none" stroke="#3a58a0" stroke-width="10" stroke-dasharray="8 5"/><circle cx="31" cy="31" r="16" fill="#fff"/><path d="M18 56 L10 82 L22 76 L28 88 L31 60Z M44 56 L52 82 L40 76 L34 88 L31 60Z" fill="#fff"/></svg>
    QUALITY
  </div>
  <div class="value">
    <svg width="110" height="95" viewBox="0 0 110 95"><circle cx="35" cy="60" r="22" fill="none" stroke="#3a58a0" stroke-width="12" stroke-dasharray="9 5"/><circle cx="35" cy="60" r="8" fill="#3a58a0"/><circle cx="82" cy="42" r="13" fill="none" stroke="#fff" stroke-width="8" stroke-dasharray="6 4"/><circle cx="55" cy="15" r="9" fill="none" stroke="#fff" stroke-width="6" stroke-dasharray="5 3"/></svg>
    TECHNOLOGY
  </div>
  <div class="value">
    <svg width="120" height="70" viewBox="0 0 120 70"><rect x="40" y="2" width="78" height="44" fill="#3a58a0"/><path d="M2 50 L2 32 L14 14 L38 14 L38 50Z" fill="#fff"/><rect x="2" y="46" width="116" height="8" fill="#fff"/><circle cx="18" cy="58" r="9" fill="#fff" stroke="#f39200" stroke-width="4"/><circle cx="70" cy="58" r="9" fill="#fff" stroke="#f39200" stroke-width="4"/><circle cx="94" cy="58" r="9" fill="#fff" stroke="#f39200" stroke-width="4"/></svg>
    PUNCTUALITY
  </div>
</section>

<p class="abs acc-title">Custom Laboratory Accessories</p>
<div class="abs acc-img" role="img" aria-label="Illustration of a V-grooved curing fixture on a blue circle"></div>
<div class="abs acc-text">
  <p>Machining of laboratory related tools:</p>
  <ul>
    <li class="mark">Gravity or pressure type V-grooved curing</li>
    <li>fixture for Tensile Bond Strength test of</li>
    <li class="mark">coating</li>
    <li class="mark">Loading fixture</li>
    <li>and more...</li>
  </ul>
</div>

<section class="abs contact">
  <p class="abs">Do not hesitate to contact us, if<br>you have any questions.</p>
  <div class="abs btn-contact">CONTACT US</div>
</section>
<div class="abs agent" role="img" aria-label="Photo of a customer support agent wearing a headset"></div>

<footer class="footer">
  <div class="abs logo logo-footer"><span class="dot"></span>brio.vantel</div>
  <p class="abs co">Ferrovane Sp. z o.o.<br>Science and Technology Park 'Brzozy'</p>
  <div class="abs foot-social"><span style="background:#3a58a0"></span><span style="background:#2b9be0"></span><span style="background:#d3281f"></span></div>
  <ul class="abs info">
    <li><svg width="26" height="28" viewBox="0 0 26 28"><path d="M13 1a9 9 0 0 0-9 9c0 7 9 17 9 17s9-10 9-17a9 9 0 0 0-9-9z" fill="#f39200"/><circle cx="13" cy="10" r="3.5" fill="#fff"/></svg>Lipowa 12 bud. 4C street</li>
    <li class="cont">05-410 Jozefow, Poland</li>
    <li><svg width="26" height="26" viewBox="0 0 26 26"><circle cx="13" cy="13" r="11" fill="none" stroke="#f39200" stroke-width="2"/><path d="M8 7l3 0 1 4-2 1a8 8 0 0 0 4 4l1-2 4 1v3c-7 0-11-4-11-11z" fill="#f39200"/></svg>phone: +48 555 010 246</li>
    <li><svg width="26" height="26" viewBox="0 0 26 26"><rect x="3" y="7" width="20" height="15" fill="none" stroke="#f39200" stroke-width="2"/><path d="M3 8l10 8 10-8" fill="none" stroke="#f39200" stroke-width="2"/></svg>email: info@ferrovane.com</li>
  </ul>
</footer>

<div class="abs bottom"><span class="copy">© 2020 - Brio Vantel All Right Reserved</span><span class="unsub">Unsubscribe</span></div>
</body>
</html>
```